I need a business card to reflect my new qualifications.
Accredited Teacher, Accredited Valuer & Accredited Judge of Patchwork Quilting.
Fennick Lane Studio
47 Marlow Road, Brenford Vic 3742
0412 378 906 fennick@brelnet.com.au

```html
<!DOCTYPE html>
<html lang="en">
<head>
<meta charset="utf-8">
<title>Fennick Lane Studio – Patchwork Quilting Business Card</title>
<link rel="stylesheet" href="https://fonts.googleapis.com/css2?family=Delius&display=swap">
<style>
  :root {
    --ink: #4a6cb8;
    --paper: #ffffff;
    --divider: #000000;
    --patch-light: #e4f1fb;
    --patch-mid: #bcdcf3;
    --patch-deep: #98c2ea;
  }
  * { margin: 0; padding: 0; box-sizing: border-box; }
  html, body {
    width: 926px;
    height: 1200px;
    overflow: hidden;
    background: var(--divider);
  }
  .canvas {
    position: relative;
    width: 926px;
    height: 1200px;
    font-family: "Delius", "Comic Sans MS", cursive;
    color: var(--ink);
  }
  .card-face {
    position: absolute;
    left: 0;
    width: 926px;
    background: var(--paper);
    overflow: hidden;
  }
  .card-face--front { top: 0; height: 593px; }
  .card-face--back { top: 602px; height: 598px; }

  .patchwork {
    position: absolute;
    left: 0;
    width: 100%;
  }
  .patchwork--top {
    top: 0;
    background:
      linear-gradient(to bottom, rgba(255,255,255,0) 70%, var(--paper) 100%),
      linear-gradient(100deg, var(--patch-mid) 0%, var(--patch-light) 30%, var(--patch-deep) 55%, var(--patch-light) 80%, var(--patch-mid) 100%);
  }
  .patchwork--bottom {
    bottom: 0;
    background:
      linear-gradient(to top, rgba(255,255,255,0) 70%, var(--paper) 100%),
      linear-gradient(80deg, var(--patch-mid) 0%, var(--patch-light) 25%, var(--patch-deep) 50%, var(--patch-light) 75%, var(--patch-mid) 100%);
  }
  .card-face--front .patchwork--top { height: 200px; }
  .card-face--front .patchwork--bottom { height: 218px; }
  .card-face--back .patchwork--top { height: 146px; }
  .card-face--back .patchwork--bottom { height: 174px; }

  .line {
    position: absolute;
    left: 0;
    width: 100%;
    text-align: center;
    white-space: nowrap;
    line-height: 1;
    font-weight: 400;
  }
  .credentials { top: 208px; font-size: 43px; letter-spacing: 0.5px; }
  .craft { top: 284px; font-size: 68px; }

  .phone { top: 172px; font-size: 56px; letter-spacing: -2px; }
  .studio-name { top: 244px; font-size: 46px; }
  .address { top: 304px; font-size: 46px; }
  .email { top: 362px; font-size: 46px; letter-spacing: -1px; }
</style>
</head>
<body>
<main class="canvas">
  <section class="card-face card-face--front">
    <div class="patchwork patchwork--top" role="img" aria-label="Soft blue hexagon patchwork pattern"></div>
    <p class="line credentials">Accredited Teacher, Valuer and Judge of</p>
    <h1 class="line craft">Patchwork Quilting</h1>
    <div class="patchwork patchwork--bottom" role="img" aria-label="Soft blue hexagon patchwork pattern"></div>
  </section>

  <section class="card-face card-face--back">
    <div class="patchwork patchwork--top" role="img" aria-label="Soft blue hexagon patchwork pattern"></div>
    <p class="line phone">0412-378-906</p>
    <p class="line studio-name">Fennick Lane Studio</p>
    <p class="line address">47 Marlow Road, Brenford Vic 3742</p>
    <p class="line email">fennick@brelnet.com.au</p>
    <div class="patchwork patchwork--bottom" role="img" aria-label="Soft blue hexagon patchwork pattern"></div>
  </section>
</main>
</body>
</html>
```